Corvane Nightclub Flyer (Updated)

Flyer for facebook, square is fine, or rectangular. Here is the text:
CORVANE
Nightclub + Lounge
presents

HALO THURSDAY
Nov 29 2018

CLUB FLOOR:
GLEN B2B ROBBY
FREDERICK TALAVERO

LOUNGE:
CARL B2B MY COUSIN
ROCKET JULES

Powered by KESTA Acoustics
4217 6th Street 21+ 9pm-2am
corvanevenuehall.com for VIP booth inquiries

Target Market(s)

Nightclub

Industry/Entity Type

Night Club

Font styles to use
Sans Serif

Colors

Designer to choose colors to be used in the design.

Requirements
Must have
• All the text listed, and plz keep the theme of the attached files. We want to stay consistent with the Corvane brand
Nice to have
• Try to stay with the theme from the attachments
Should not have
• Dont' stray to far from the general theme we have from the attachments

```html
<!DOCTYPE html>
<html lang="en">
<head>
<meta charset="utf-8">
<title>Corvane Nightclub + Lounge — Halo Thursday</title>
<link rel="stylesheet" href="https://fonts.googleapis.com/css2?family=Lato:wght@400;700;900&family=Fira+Sans:wght@400&display=swap">
<style>
  :root {
    --pink: #e8215e;
    --pink-deep: #d81b54;
    --silver: #c8c8cc;
    --white: #ffffff;
    --lime: #d6e38c;
    --panel: rgba(6, 8, 14, 0.72);
    --night-1: #05070d;
    --night-2: #0c1d3c;
    --night-3: #1b4f8a;
    --teal: #2f8f7a;
  }
  * { margin: 0; padding: 0; box-sizing: border-box; }
  html, body { width: 1200px; height: 1200px; overflow: hidden; background: var(--night-1); }
  .flyer {
    position: relative;
    width: 1200px;
    height: 1200px;
    overflow: hidden;
    font-family: "Lato", sans-serif;
    color: var(--white);
  }
  .crowd-scene {
    position: absolute; inset: 0;
    background:
      radial-gradient(ellipse 520px 260px at 640px 120px, rgba(47,143,122,0.55), transparent 70%),
      radial-gradient(ellipse 420px 380px at 160px 430px, rgba(40,110,200,0.6), transparent 70%),
      radial-gradient(ellipse 500px 300px at 520px 260px, rgba(30,90,60,0.45), transparent 70%),
      linear-gradient(180deg, var(--night-2) 0%, #0a1426 45%, var(--night-1) 100%);
  }
  .shapes { position: absolute; inset: 0; }
  .venue-name {
    position: absolute; left: 46px; top: 34px;
    font-weight: 900; font-size: 150px; letter-spacing: 8px; line-height: 1;
    color: var(--pink);
    -webkit-text-stroke: 5px var(--silver);
    paint-order: stroke fill;
  }
  .venue-type {
    position: absolute; left: 60px; top: 236px;
    font-weight: 700; font-size: 42px; letter-spacing: 6px;
  }
  .presents {
    position: absolute; left: 78px; top: 326px; width: 486px; height: 58px;
    display: flex; align-items: center; justify-content: center;
    font-size: 38px; letter-spacing: 12px;
  }
  .event-title {
    position: absolute; left: 24px; top: 568px; width: 612px; text-align: center;
    font-size: 66px; line-height: 1;
  }
  .event-date {
    position: absolute; left: 24px; top: 646px; width: 612px; text-align: center;
    font-size: 48px; letter-spacing: 6px; line-height: 1;
  }
  .lineup {
    position: absolute; right: 54px; text-align: right;
    font-size: 36px; line-height: 47px; text-transform: uppercase;
  }
  .lineup .room { color: var(--pink); letter-spacing: 2px; }
  .lineup--club { top: 375px; }
  .lineup--lounge { top: 675px; }
  .powered {
    position: absolute; left: 56px; top: 918px;
    font-family: "Fira Sans", sans-serif; font-size: 38px; color: var(--lime);
  }
  .details {
    position: absolute; left: 56px; top: 1010px;
    font-family: "Fira Sans", sans-serif; font-size: 26px; line-height: 33px; color: var(--lime);
  }
  .brand-mark {
    position: absolute; left: 790px; top: 844px; width: 352px; height: 350px;
    display: flex; flex-direction: column; align-items: center; justify-content: center; gap: 26px;
  }
  .brand-mark .dot {
    width: 110px; height: 110px; border-radius: 50%; background: var(--lime);
  }
  .brand-mark .name {
    font-size: 52px; letter-spacing: 3px; color: var(--silver);
  }
</style>
</head>
<body>
<main class="flyer">
  <div class="crowd-scene" role="img" aria-label="Nightclub dance floor with a crowd under blue stage lights and hanging greenery"></div>

  <svg class="shapes" width="1200" height="1200" viewBox="0 0 1200 1200" aria-hidden="true">
    <rect class="lineup-panel" x="718" y="314" width="482" height="886" fill="var(--panel)"/>
    <line x1="718" y1="600" x2="1200" y2="600" stroke="var(--pink)" stroke-width="3"/>
    <rect class="brand-frame" x="790" y="844" width="352" height="350" fill="none" stroke="var(--pink)" stroke-width="3"/>

    <g class="presents-banner" fill="var(--pink)">
      <rect x="78" y="330" width="486" height="52"/>
      <rect x="62" y="318" width="18" height="76" rx="6"/>
      <rect x="562" y="318" width="18" height="76" rx="6"/>
      <rect x="56" y="314" width="30" height="10" rx="5"/>
      <rect x="56" y="388" width="30" height="10" rx="5"/>
      <rect x="556" y="314" width="30" height="10" rx="5"/>
      <rect x="556" y="388" width="30" height="10" rx="5"/>
    </g>

    <path class="event-badge" d="M36,476 Q330,512 624,476 Q586,636 624,796 Q330,760 36,796 Q74,636 36,476 Z"
          fill="var(--pink-deep)" fill-opacity="0.92" stroke="var(--silver)" stroke-width="6"/>

    <line x1="0" y1="982" x2="606" y2="982" stroke="var(--pink)" stroke-width="3"/>
  </svg>

  <h1 class="venue-name">CORVANE</h1>
  <p class="venue-type">Nightclub+Lounge</p>
  <p class="presents">presents</p>

  <h2 class="event-title">HALO THURSDAY</h2>
  <p class="event-date">Nov 29 2018</p>

  <div class="lineup lineup--club">
    <p class="room">Club Floor:</p>
    <p>Glen B2B Robby</p>
    <p>Frederick Talavero</p>
  </div>

  <div class="lineup lineup--lounge">
    <p class="room">Lounge:</p>
    <p>Carl B2B My Cousin</p>
    <p>Rocket Jules</p>
  </div>

  <p class="powered">Powered by KESTA Acoustics</p>
  <p class="details">4217 6th Street, 21+ 9pm-2am<br>corvanevenuehall.com<br>for VIP booth inquiries</p>

  <div class="brand-mark">
    <span class="dot"></span>
    <span class="name">CORVANE</span>
  </div>
</main>
</body>
</html>
```